Kelvar Systems Website

Website design for our company: Kelvar Systems.
The website should look fresh and IT focused. Please have a look at http://www.kelvarsystems.net.au/ for our current design. We want something fresh and new, professional looking, in WordPress so we can easily make changes.

Industry/Entity Type

It Company

```html
<!DOCTYPE html>
<html lang="en">
<head>
<meta charset="utf-8">
<title>Kelvar Systems</title>
<link href="https://fonts.googleapis.com/css2?family=Open+Sans:wght@300;400;600;700&display=swap" rel="stylesheet">
<style>
:root{
  --green:#0fae55;
  --green-bright:#16b862;
  --header:#3c3d45;
  --header-dark:#2e2f36;
  --blue:#2a86d4;
  --blue-light:#3f9be6;
  --ink:#3a3b40;
  --muted:#6b6c70;
  --panel-grey:#e6e6e6;
  --quote-grey:#8d8e92;
  --footer:#46474c;
  --footer-text:#c9cacc;
  --white:#ffffff;
}
*{box-sizing:border-box;margin:0;padding:0}
html,body{width:1024px;height:1200px;overflow:hidden}
body{font-family:"Open Sans",sans-serif;background:var(--white);position:relative;color:var(--ink)}
.abs{position:absolute}

/* header */
.site-header{position:absolute;left:0;top:0;width:1024px;height:82px;background:linear-gradient(#43444c,var(--header-dark));border-top:5px solid var(--green)}
.brand{position:absolute;left:138px;top:0;width:148px;height:70px;background:var(--green);border:2px solid #fff;border-top:none;display:flex;align-items:center;justify-content:center;gap:7px}
.brand-dot{width:14px;height:14px;border-radius:50%;background:#fff}
.brand-name{color:#fff;font-weight:700;font-size:15px}
.search{position:absolute;left:734px;top:12px;width:138px;height:17px;background:#fff;border:1px solid #ccc;font-size:8px;color:#777;padding:3px 0 0 20px}
.search svg{position:absolute;left:5px;top:3px}
.main-nav{position:absolute;left:318px;top:37px;display:flex;gap:0}
.main-nav a{display:block;color:#fff;font-weight:700;font-size:12px;text-decoration:none;height:25px;line-height:25px}
.main-nav a.active{background:linear-gradient(var(--blue-light),#1f72c2);padding:0 12px;border-radius:2px;border:1px solid #5aaef0}

/* hero */
.hero-photo{position:absolute;left:0;top:82px;width:1024px;height:365px;background:linear-gradient(100deg,#cfdbe6 0%,#8aa6c4 25%,#2c4c78 45%,#e8eef4 70%,#c8dcec 100%)}
.hero-card{position:absolute;left:650px;top:126px;width:236px;height:278px;background:var(--green-bright);color:#fff;padding:32px 23px}
.hero-card h1{font-size:24px;font-weight:700;line-height:29px}
.hero-card p{font-size:11.5px;line-height:16px;margin-top:15px}
.dots{display:flex;gap:8px;margin-top:40px}
.dots span{width:8px;height:8px;border-radius:50%;background:rgba(255,255,255,.45)}
.dots span.on{background:#fff}

/* remote band */
.remote-band{position:absolute;left:0;top:447px;width:1024px;height:84px;background:radial-gradient(ellipse at 45% 0%,#44c982 0%,var(--green) 55%)}
.remote-band h2{position:absolute;left:162px;top:17px;color:#fff;font-weight:300;font-size:23px}
.remote-band p{position:absolute;left:162px;top:46px;color:#fff;font-size:14.5px}
.code-input{position:absolute;left:616px;top:30px;width:176px;height:30px;background:#fff;border:1px solid #ddd;font-size:12px;color:#666;padding:7px 11px}
.connect-btn{position:absolute;left:800px;top:30px;width:87px;height:30px;background:linear-gradient(var(--blue-light),#2479c9);color:#fff;font-weight:700;font-size:12px;text-align:center;line-height:30px;border-radius:2px}

/* services */
.section-title{position:absolute;left:0;width:1024px;text-align:center;font-weight:300;font-size:20px;color:var(--ink)}
.divider{position:absolute;left:141px;top:595px;width:752px;height:2px;background:#dcdcdc}
.divider:after{content:"";position:absolute;left:370px;top:2px;border:5px solid transparent;border-top-color:#dcdcdc}
.service{position:absolute;display:flex;align-items:center;gap:8px;font-weight:700;font-size:11.5px;color:var(--ink);line-height:16px}
.service .ico{width:32px;height:32px;border-radius:50%;background:#3b3c42;display:flex;align-items:center;justify-content:center;flex:none;box-shadow:0 0 0 2px #e2e2e2}
.service.current{color:var(--blue)}
.service.current .ico{background:var(--blue)}

/* about & testimonial */
.about-band{position:absolute;left:0;top:770px;width:1024px;height:207px;background:var(--panel-grey)}
.band-title{position:absolute;font-weight:300;font-size:20px;color:var(--ink)}
.avatar{position:absolute;border-radius:50%;background:radial-gradient(#9a9a9a,#555);border:3px solid #fff;box-shadow:0 0 0 1px #bbb}
.body-copy{position:absolute;font-size:10.5px;line-height:16px;color:var(--ink)}
.read-more{position:absolute;left:223px;top:919px;width:83px;height:26px;background:#efefef;border:1px solid #ccc;border-radius:3px;font-size:7.5px;text-align:center;line-height:25px;color:#444}
.quote-box{position:absolute;left:617px;top:838px;width:276px;height:105px;background:var(--quote-grey);border-bottom:3px solid #b3b4b7;color:#fff;font-size:10.5px;line-height:16px;padding:24px 25px 0 25px;border-radius:2px}
.quote-box:before{content:"";position:absolute;left:-18px;top:14px;border:9px solid transparent;border-right-color:var(--quote-grey);border-top-color:var(--quote-grey)}
.quote-mark{position:absolute;right:10px;top:-26px;font-size:110px;font-weight:700;color:rgba(0,0,0,.12);font-family:Georgia,serif}
.person{position:absolute;left:526px;top:893px;font-size:7.5px;color:#333;line-height:10px}
.person b{font-size:8.5px}

/* footer */
.site-footer{position:absolute;left:0;top:977px;width:1024px;height:216px;background:var(--footer)}
.site-footer:after{content:"";position:absolute;left:0;top:216px;width:1024px;height:7px;background:var(--green)}
.footer-brand{position:absolute;left:142px;top:34px;width:150px;height:54px;background:var(--green);border:2px solid #fff;border-radius:2px;display:flex;align-items:center;justify-content:center;gap:7px}
.footer-head{position:absolute;top:36px;font-weight:700;font-size:11.5px;color:#c7c8ca}
.footer-nav{position:absolute;left:370px;top:65px;list-style:none;font-size:10.5px;color:var(--footer-text);line-height:16px}
.footer-nav li:before{content:"";display:inline-block;border:3px solid transparent;border-left:4px solid var(--footer-text);margin-right:4px}
.footer-contact{position:absolute;left:526px;top:64px;font-style:normal;font-size:10.5px;line-height:16px;color:var(--footer-text)}
.footer-note{position:absolute;left:718px;top:66px;font-size:9.5px;color:var(--footer-text)}
.footer-input{position:absolute;left:718px;top:91px;width:175px;height:26px;background:#3d3e42;border:1px solid #5a5b60;border-radius:3px}
.footer-input span{position:absolute;right:0;top:0;height:24px;width:55px;border-left:1px solid #5a5b60;font-size:7.5px;color:#ccc;text-align:center;line-height:24px}
.social{position:absolute;left:718px;top:161px;display:flex;gap:16px}
.social span{width:12px;height:12px;border-radius:50%;background:#6b6c70}
.copyright{position:absolute;left:142px;top:161px;font-size:9.5px;color:#7f8084}
</style>
</head>
<body>

<header class="site-header">
  <div class="brand"><span class="brand-dot"></span><span class="brand-name">Kelvar Systems</span></div>
  <div class="search">
    <svg width="9" height="9" viewBox="0 0 10 10"><circle cx="4" cy="4" r="3" fill="none" stroke="#999" stroke-width="1.3"/><line x1="6.2" y1="6.2" x2="9" y2="9" stroke="#999" stroke-width="1.3"/></svg>
    Search Site
  </div>
  <nav class="main-nav">
    <a class="active" href="#">Home</a>
    <a href="#" style="margin-left:30px">Services</a>
    <a href="#" style="margin-left:39px">Support</a>
    <a href="#" style="margin-left:36px">Clients</a>
    <a href="#" style="margin-left:39px">Testimonial</a>
    <a href="#" style="margin-left:40px">About</a>
    <a href="#" style="margin-left:38px">Contact</a>
  </nav>
</header>

<div class="hero-photo" role="img" aria-label="Photo of three smiling business people giving a thumbs up in a bright office"></div>
<section class="hero-card">
  <h1>We will bring your businesses forward</h1>
  <p>Kelvar Systems is an Adelaide based company with a single objective - to excel in the support and service of all computer and IT needs.</p>
  <div class="dots"><span class="on"></span><span></span><span></span><span></span></div>
</section>

<section class="remote-band">
  <h2>Remote Support</h2>
  <p>Need help? Connect to our friendly staff to assist you.</p>
  <div class="code-input">Enter 6-digit Code</div>
  <div class="connect-btn">Connect</div>
</section>

<h2 class="section-title" style="top:553px">OUR SERVICES</h2>
<div class="divider"></div>

<div class="service current" style="left:141px;top:623px"><span class="ico"><svg width="14" height="14" viewBox="0 0 14 14"><circle cx="7" cy="7" r="6" fill="#fff"/><rect x="4" y="5.5" width="6" height="1" fill="#2a86d4"/><rect x="4" y="7.5" width="6" height="1" fill="#2a86d4"/></svg></span>ON-SITE SERVICE</div>
<div class="service" style="left:333px;top:623px"><span class="ico"><svg width="14" height="14" viewBox="0 0 14 14" fill="none" stroke="#fff" stroke-width="1.4"><rect x="3" y="3" width="8" height="8"/><rect x="1" y="1" width="3" height="3" fill="#fff"/><rect x="10" y="1" width="3" height="3" fill="#fff"/><rect x="1" y="10" width="3" height="3" fill="#fff"/><rect x="10" y="10" width="3" height="3" fill="#fff"/></svg></span>MEDICAL IT SERVICE</div>
<div class="service" style="left:526px;top:623px"><span class="ico"><svg width="16" height="16" viewBox="0 0 16 16"><circle cx="8" cy="8" r="7" fill="#fff"/><path d="M4 5c2 0 3 2 2 4s1 3 2 4M10 3c0 2 2 3 4 3" stroke="#3b3c42" stroke-width="1.5" fill="none"/></svg></span>REMOTE DESKTOP</div>
<div class="service" style="left:718px;top:623px"><span class="ico"><svg width="14" height="14" viewBox="0 0 14 14"><rect x="6" y="1" width="2" height="4" fill="#fff"/><path d="M5 5h4l4 8H1z" fill="#fff"/></svg></span>PHARMACY IT SERVICE</div>

<div class="service" style="left:141px;top:682px"><span class="ico"><svg width="12" height="14" viewBox="0 0 12 14" fill="none" stroke="#fff" stroke-width="1.3"><path d="M1 1h7l3 3v9H1z"/><circle cx="5" cy="8" r="1.5"/><circle cx="8" cy="10" r="1.2"/></svg></span>HARDWARE/ SOFTWARE<br>SUPPLY</div>
<div class="service" style="left:333px;top:682px"><span class="ico"><svg width="14" height="14" viewBox="0 0 14 14"><path d="M12 1L5 9l1 1 7-8z" fill="#fff"/><path d="M4 10c-2 0-2 2-3 3 2 0 4 0 4-2z" fill="#fff"/></svg></span>WEBSITE DESIGN</div>
<div class="service" style="left:526px;top:682px"><span class="ico"><svg width="16" height="16" viewBox="0 0 16 16" fill="#fff"><path d="M8 1l3 3-3 3-1-1 2-2-2-2zM8 15l-3-3 3-3 1 1-2 2 2 2z"/><path d="M2 8l3-3 1 1-2 2 2 2-1 1zM14 8l-3 3-1-1 2-2-2-2 1-1z"/></svg></span>DISASTER RECOVERY</div>
<div class="service" style="left:718px;top:682px"><span class="ico"><svg width="14" height="14" viewBox="0 0 14 14" fill="#fff"><rect x="1" y="1" width="1.5" height="12"/><rect x="4.3" y="1" width="1.5" height="12"/><rect x="7.6" y="1" width="1.5" height="12"/><rect x="11" y="1" width="1.5" height="12"/><rect x="0" y="4" width="3.5" height="2"/><rect x="3.3" y="8" width="3.5" height="2"/><rect x="6.6" y="5" width="3.5" height="2"/><rect x="10" y="9" width="3.5" height="2"/></svg></span>CONSUMABLES</div>

<section class="about-band"></section>
<h2 class="band-title" style="left:142px;top:796px">WELCOME TO OUR SITE!</h2>
<div class="avatar" role="img" aria-label="Portrait photo of a smiling man" style="left:143px;top:837px;width:68px;height:68px"></div>
<p class="body-copy" style="left:223px;top:834px;width:255px">Because we know you don't want to be limited on a portrait or scape format we made Showcase. compatible in both portrait AND landscape! Yes, we care about you.</p>
<div class="read-more">READ MORE</div>

<h2 class="band-title" style="left:526px;top:796px">WHAT PEOPLE SAY</h2>
<div class="avatar" role="img" aria-label="Portrait photo of a smiling woman" style="left:526px;top:837px;width:52px;height:52px"></div>
<div class="person"><b>MARA ELLISON</b><br>CEO, ELLISONCO.COM</div>
<blockquote class="quote-box"><span class="quote-mark">&#8220;</span>Because we know you don't want to be limited on a portrait or scape format we made Showcase. compatible in both portrait AND landscape!</blockquote>

<footer class="site-footer">
  <div class="footer-brand"><span class="brand-dot"></span><span class="brand-name">Kelvar Systems</span></div>
  <h3 class="footer-head" style="left:370px">NAVIGATION</h3>
  <ul class="footer-nav">
    <li>HOME</li><li>CLIENTS</li><li>SERVICES</li><li>SUPPORTS</li><li>TESTIMONIALS</li><li>CONTACT US</li><li>ABOUT US</li>
  </ul>
  <h3 class="footer-head" style="left:526px">CONTACTS</h3>
  <address class="footer-contact">Harbourline Pty<br>PO Box 40512<br>Wattle Lane, Brightwater<br>Victoria 3999 Australia<br><br>Phone: (03) 5550 1427<br>help@kelvarsystems.net.au</address>
  <h3 class="footer-head" style="left:718px">REMOTE SUPPORT</h3>
  <p class="footer-note">Enter you 6-digit code</p>
  <div class="footer-input"><span>CONNECT</span></div>
  <h3 class="footer-head" style="left:718px;top:143px">GET SOCIAL</h3>
  <div class="social"><span></span><span></span><span></span><span></span><span></span></div>
  <p class="copyright">© 2014 Kelvar Systems. All Rights Reserved</p>
</footer>

</body>
</html>
```